Professional Business Cards

We need a nice looking, profession and modern business card for our new company. Our logo is attatched

Target Market(s)

Young Professionals

Industry/Entity Type

Financial

Contact Information for Business Card

FRONT

Morvane Tally Pty Ltd
Level 22, Halden Court, 48 Wirrapool St
Sydney NSW 2000
ABN : 57 304 918 226

Derek Wallis - Chief Operations Officer
P : 02 7153 2819
M: 0418 395 207
derek@morvanetally,com

BACK

- Cryptocurrency Exchange Services
- Cryptocurrency Mining Operations
- Cryptocurrency Investment Fund Offering

Font styles to use
Sans Serif

Colors
0255a3
9d9d9d

```html
<!DOCTYPE html>
<html lang="en">
<head>
<meta charset="utf-8">
<title>Morvane Tally – Business Card</title>
<link rel="stylesheet" href="https://fonts.googleapis.com/css2?family=Roboto:wght@400;500;700&display=swap">
<style>
  :root {
    --brand-blue: #0255a3;
    --brand-grey: #9d9d9d;
    --strip-grey: #6e6e72;
    --paper: #ffffff;
    --backdrop: #3a3a3c;
  }
  html, body {
    margin: 0;
    padding: 0;
    width: 1200px;
    height: 900px;
    overflow: hidden;
    background: var(--backdrop);
    font-family: "Roboto", Arial, sans-serif;
  }
  .canvas {
    position: relative;
    width: 1200px;
    height: 900px;
  }
  .card {
    position: absolute;
    left: 260px;
    width: 680px;
    height: 390px;
    overflow: hidden;
    box-shadow: 0 10px 30px rgba(0,0,0,0.45);
  }

  /* Back side */
  .card-back {
    top: 40px;
    background: var(--paper);
  }
  .card-back .brand {
    position: absolute;
    top: 100px;
    left: 0;
    right: 0;
    display: flex;
    align-items: center;
    justify-content: center;
    gap: 16px;
  }
  .brand-square {
    width: 40px;
    height: 40px;
    background: var(--brand-blue);
  }
  .brand-name {
    color: var(--brand-blue);
    font-weight: 700;
    font-size: 46px;
    letter-spacing: 1px;
    text-transform: uppercase;
  }
  .card-back .rule {
    position: absolute;
    left: 0;
    right: 0;
    top: 238px;
    height: 6px;
    background: var(--strip-grey);
  }
  .card-back .service-band {
    position: absolute;
    left: 0;
    right: 0;
    top: 250px;
    bottom: 0;
    background: var(--brand-blue);
    color: var(--paper);
    display: flex;
    flex-direction: column;
    align-items: center;
    justify-content: center;
    gap: 8px;
    font-size: 17px;
    font-weight: 500;
  }
  .service-row { display: flex; align-items: center; gap: 12px; }
  .diamond {
    width: 7px; height: 7px; background: var(--paper);
    transform: rotate(45deg);
  }

  /* Front side */
  .card-front {
    top: 470px;
    background: var(--brand-blue);
  }
  .card-front .brand-mark {
    position: absolute;
    left: 40px;
    top: 120px;
    width: 230px;
    display: flex;
    align-items: center;
    gap: 12px;
    color: var(--paper);
    font-weight: 700;
    font-size: 26px;
    text-transform: uppercase;
  }
  .brand-mark .brand-square { background: var(--paper); width: 34px; height: 34px; flex: none; }
  .card-front .divider {
    position: absolute;
    left: 290px;
    top: 60px;
    width: 2px;
    height: 190px;
    background: linear-gradient(to bottom, rgba(255,255,255,0), rgba(255,255,255,0.75) 50%, rgba(255,255,255,0));
  }
  .contact {
    position: absolute;
    left: 320px;
    top: 58px;
    color: var(--paper);
    font-size: 17px;
    line-height: 1.32;
  }
  .contact .person-name,
  .contact .person-title {
    font-weight: 700;
    text-transform: uppercase;
    font-size: 19px;
  }
  .contact .person-title { margin-bottom: 4px; }
  .contact-line { display: flex; align-items: center; gap: 10px; }
  .contact-line svg { width: 17px; height: 17px; flex: none; }
  .card-front .base-rule {
    position: absolute;
    left: 0; right: 0;
    bottom: 44px;
    height: 4px;
    background: var(--paper);
  }
  .card-front .base-strip {
    position: absolute;
    left: 0; right: 0;
    bottom: 0;
    height: 44px;
    background: var(--strip-grey);
  }
</style>
</head>
<body>
<main class="canvas">

  <section class="card card-back" aria-label="Card back">
    <div class="brand">
      <span class="brand-square"></span>
      <span class="brand-name">Morvane Tally</span>
    </div>
    <div class="rule"></div>
    <div class="service-band">
      <div class="service-row">
        <span>Cryptocurrency Exchange Services</span>
        <span class="diamond"></span>
        <span>Cryptocurrency Mining Operations</span>
      </div>
      <div>Cryptocurrency Investment Fund Offering</div>
    </div>
  </section>

  <section class="card card-front" aria-label="Card front">
    <div class="brand-mark">
      <span class="brand-square"></span>
      <span>Morvane Tally</span>
    </div>
    <div class="divider"></div>
    <div class="contact">
      <div class="person-name">Derek Wallis</div>
      <div class="person-title">Chief Operations Officer</div>
      <div>Level 22, Halden Court, 48 Wirrapool St</div>
      <div>Sydney NSW 2000</div>
      <div>ABN : 57 304 918 226</div>
      <div class="contact-line">
        <svg viewBox="0 0 24 24" aria-hidden="true"><path fill="#fff" d="M6.6 10.8a15 15 0 0 0 6.6 6.6l2.2-2.2a1 1 0 0 1 1-.25 11.4 11.4 0 0 0 3.6.57 1 1 0 0 1 1 1V20a1 1 0 0 1-1 1A17 17 0 0 1 3 4a1 1 0 0 1 1-1h3.5a1 1 0 0 1 1 1c0 1.25.2 2.45.57 3.57a1 1 0 0 1-.25 1z"/></svg>
        <span>02.7153.2819</span>
      </div>
      <div class="contact-line">
        <svg viewBox="0 0 24 24" aria-hidden="true"><rect x="6" y="2" width="12" height="20" rx="2" fill="none" stroke="#fff" stroke-width="2"/><circle cx="12" cy="18" r="1.2" fill="#fff"/></svg>
        <span>0418.395.207</span>
      </div>
      <div class="contact-line">
        <svg viewBox="0 0 24 24" aria-hidden="true"><rect x="2" y="5" width="20" height="14" fill="none" stroke="#fff" stroke-width="2"/><path d="M2 5l10 8 10-8" fill="none" stroke="#fff" stroke-width="2"/></svg>
        <span>derek@morvanetally,com</span>
      </div>
    </div>
    <div class="base-rule"></div>
    <div class="base-strip"></div>
  </section>

</main>
</body>
</html>
```